Louisiana personal injury attorney needs a postcard design

This will be the first of three post cards to go out to previous clients. We do not have intentions of making all three match/work with each other, but if you have an idea for that, please, let us know! This is for an attorney in Lafayette, LA that specializes in Medical Malpractice and Personal Injury. We would like the front of the post card to focus on those two practice areas and really grab someones attention!

the card in general will say: Glad to have served you, come see us for a free T-shirt, have a cup of coffee with us…

Please use a photo of the office for us to use on the back with a map of the office location (will send location when we pick the winner)

Industry/Entity Type

Legal

Font styles to use
Serif
Sans Serif

Requirements
Must have
• map of location of office. Large image or several images on the front. attention grabbing
Nice to have
• colors that match the logo. clean and easy to follow
Should not have
• should not be messy or too much going on.

```html
<!DOCTYPE html>
<html lang="en">
<head>
<meta charset="utf-8">
<title>Bellard Law Firm – Client Postcard</title>
<link href="https://fonts.googleapis.com/css2?family=Montserrat:wght@500;600;700;800&display=swap" rel="stylesheet">
<style>
  :root {
    --stage: #e4e4e4;
    --slate: #5e5853;
    --slate-light: #6b655f;
    --gold: #c8962a;
    --paper: #ffffff;
    --paper-back: #ededed;
    --ink: #2a2a2a;
    --line: #333333;
  }
  * { margin: 0; padding: 0; box-sizing: border-box; }
  html, body { width: 1200px; height: 1005px; overflow: hidden; }
  body {
    background: var(--stage);
    font-family: "Montserrat", Arial, sans-serif;
    display: flex; flex-direction: column; align-items: center;
    gap: 30px; padding-top: 27px;
  }
  .postcard {
    position: relative; width: 690px; height: 460px; overflow: hidden;
    box-shadow: 0 6px 18px rgba(0,0,0,.18);
  }
  .postcard-front { background: var(--slate); }
  .front-shapes { position: absolute; inset: 0; }
  .office-photo-main {
    position: absolute; left: 300px; top: 240px; right: 0; bottom: 0;
    background: linear-gradient(160deg, #a9bccd 0%, #5a6577 40%, #3f4756 72%, #5f8a3e 100%);
  }
  .brand {
    position: absolute; display: flex; align-items: center; gap: 10px;
    color: var(--gold); font-weight: 800; letter-spacing: 1px;
  }
  .brand-mark { width: 14px; height: 14px; background: var(--gold); }
  .front-brand { top: 62px; right: 40px; font-size: 34px; }
  .headline { position: absolute; left: 38px; top: 138px; color: var(--gold); }
  .headline-big { font-size: 86px; font-weight: 800; line-height: 1; letter-spacing: -1px; }
  .headline-sub { font-size: 29px; font-weight: 800; line-height: 1.2; margin-top: 8px; }
  .invite {
    position: absolute; left: 38px; top: 318px; width: 180px;
    color: #fff; font-size: 18px; font-weight: 500; line-height: 1.3;
  }
  .invite p + p { margin-top: 12px; }

  .postcard-back { background: linear-gradient(135deg, #f6f6f6, var(--paper-back)); }
  .back-brand { top: 34px; left: 60px; font-size: 28px; }
  .back-tagline {
    position: absolute; top: 82px; left: 60px; width: 360px;
    font-size: 15px; font-weight: 700; color: var(--ink); line-height: 1.25;
  }
  .map-frame {
    position: absolute; left: 60px; top: 160px; width: 340px; height: 210px;
    border: 4px solid var(--ink); border-radius: 20px;
    background: linear-gradient(135deg, #eef1f3, #dfe5e9 60%, #cfe3ec);
  }
  .office-photos { position: absolute; top: 160px; left: 425px; display: flex; gap: 10px; }
  .office-photo {
    width: 115px; height: 78px; border: 3px solid var(--ink); border-radius: 14px;
    background: linear-gradient(135deg, #8a7a68, #4a4642 55%, #3d6c92);
  }
  .address-line { position: absolute; left: 425px; width: 225px; height: 2px; background: var(--line); }
</style>
</head>
<body>

<section class="postcard postcard-front">
  <svg class="front-shapes" width="690" height="460" viewBox="0 0 690 460">
    <rect width="690" height="460" fill="var(--slate)"/>
    <polygon points="0,0 690,0 690,115 430,225" fill="var(--paper)"/>
  </svg>
  <div class="office-photo-main" role="img" aria-label="Photograph of the law firm's office building"></div>
  <div class="brand front-brand"><span class="brand-mark"></span>BELLARD LAW FIRM</div>
  <div class="headline">
    <div class="headline-big">GLAD</div>
    <div class="headline-sub">TO HAVE<br>SERVED YOU</div>
  </div>
  <div class="invite">
    <p>come see us for a FREE T-SHIRT,</p>
    <p>have a cup of coffee with us…</p>
  </div>
</section>

<section class="postcard postcard-back">
  <div class="brand back-brand"><span class="brand-mark"></span>BELLARD LAW FIRM</div>
  <p class="back-tagline">Lorem ipsum dolor sit amet, consectetuer adipiscing elit, sed diam nonummy nibh euismod</p>
  <div class="map-frame" role="img" aria-label="Street map showing the office location"></div>
  <div class="office-photos">
    <div class="office-photo" role="img" aria-label="Photograph of the office conference room"></div>
    <div class="office-photo" role="img" aria-label="Photograph of the office meeting area"></div>
  </div>
  <div class="address-line" style="top:280px"></div>
  <div class="address-line" style="top:320px"></div>
  <div class="address-line" style="top:360px"></div>
</section>

</body>
</html>
```